Web design

We need the design for the logo and website for a women fashion website. No coding required. The colors used should be neutral (maybe with a light touch of color), the style should be modern, slightly luxurious, not too crowded. The target market is young professionals who love trendy clothes.
Updates

Need extra days to review

Target Market(s)

Young professionals

Industry/Entity Type

Apparel

Number of Pages Required

5+ page

Font styles to use
Sans Serif
Other font styles liked:
• Montserrat, Engravers Gothic, Benton Sans, gotham-book

Colors

Designer to choose colors to be used in the design.

```html
<!DOCTYPE html>
<html lang="en">
<head>
<meta charset="utf-8">
<title>OSSA – Web Design Boards</title>
<link href="https://fonts.googleapis.com/css2?family=Montserrat:wght@300;400;500;600;800&display=swap" rel="stylesheet">
<style>
:root{
  --board:#a9a9a9;
  --paper:#ffffff;
  --ink:#1d1d24;
  --black:#000000;
  --gold:#f1c96b;
  --tan:#d2b68e;
  --grey-text:#555555;
}
*{box-sizing:border-box;margin:0;padding:0}
html,body{width:1200px;height:1200px;overflow:hidden}
body{background:var(--board);font-family:'Montserrat',sans-serif;color:var(--ink);position:relative}
.page{position:absolute;background:var(--paper);overflow:hidden}
.page > *{position:absolute}
.brand-name{left:0;width:366px;top:19px;text-align:center;font-size:13px;font-weight:500;letter-spacing:1px}
.nav{top:40px;font-size:3.6px;letter-spacing:1px;color:var(--tan);font-weight:600;white-space:nowrap}
.section-title{left:0;width:372px;text-align:center;font-size:7.5px;letter-spacing:2.5px;color:var(--tan);font-weight:600}
.tile-text{color:#fff;font-size:10px;font-weight:300;letter-spacing:1px;line-height:1.05}
.tile-text b{font-weight:800;letter-spacing:.5px}
.tile-text small{display:block;font-size:7px;margin-top:5px;letter-spacing:.5px}
.go{width:24px;height:12px;fill:none;stroke:var(--gold);stroke-width:2.2;stroke-linecap:round;stroke-linejoin:round}
.product-photo{background:linear-gradient(90deg,#cfcfcd 0%,#c4c4c2 22%,#1b1b1b 38%,#262626 55%,#8f7f72 68%,#c8c8c6 82%,#d2d2d0 100%)}
.product-title{font-size:7px;letter-spacing:1px;text-align:center;font-weight:400;white-space:nowrap}
.product-note{font-size:3.4px;text-align:center;color:var(--grey-text);letter-spacing:.3px;white-space:nowrap}
.card-icons{font-size:4px;color:#777}
.more{font-size:4.6px;color:var(--tan);letter-spacing:1.2px;font-weight:600}
.filter{font-size:5px;letter-spacing:1.6px;color:var(--tan);font-weight:600;white-space:nowrap}
.filter::after{content:"";display:inline-block;margin-left:3px;border-left:3.5px solid transparent;border-right:3.5px solid transparent;border-top:4px solid var(--tan);vertical-align:middle}
.social-avatar{width:46px;height:46px;border-radius:50%;background:radial-gradient(circle at 50% 40%,#eee6da 0%,#c9b9a4 40%,#7f8d99 100%)}
.social-caption{font-size:3.2px;text-align:center;width:60px;color:#444;white-space:nowrap}
.footer{left:0;width:366px;height:92px;background:var(--black);color:#fff}
.footer > *{position:absolute}
.footer .brand-name{left:23px;width:auto;top:28px;text-align:left;font-size:13px;font-weight:600}
.footer-copy{left:23px;top:47px;width:52px;font-size:2.4px;line-height:1.45}
.footer-legal{left:23px;top:72px;font-size:2.6px;letter-spacing:.3px}
.subscribe{left:215px;width:130px;top:17px;text-align:center;font-size:6.8px;font-weight:800;letter-spacing:1px}
.subscribe-note{left:206px;width:140px;top:27px;text-align:center;font-size:2.8px;letter-spacing:.3px}
.email-label{left:226px;top:41px;font-size:2.8px;font-weight:600}
.email-line{left:226px;top:53px;width:89px;height:0;border-top:.6px solid #888}
.footer .go{left:320px;top:40px}
.social-row{left:250px;top:66px;display:flex;gap:11px}
.social-row span{width:6px;height:6px;border:1px solid #fff;border-radius:50%}
.login-title{font-size:11.5px;font-weight:300;letter-spacing:2px}
.field-label{font-size:5.5px;letter-spacing:1.2px}
.field-line{height:0;border-top:.7px solid #777;width:89px}
.account-item{font-size:6px;letter-spacing:.8px}
.account-item small{display:block;font-size:4.4px;letter-spacing:.3px}
</style>
</head>
<body>

<!-- Home page -->
<section class="page" style="left:24px;top:24px;width:366px;height:1142px">
  <div class="brand-name">OSSA</div>
  <span class="nav" style="left:89px">LATEST ARRIVALS</span>
  <span class="nav" style="left:157px">CLOTHES</span>
  <span class="nav" style="left:204px">ON SALE</span>
  <span class="nav" style="left:245px">OSSA CLUB</span>

  <div role="img" aria-label="Black and white photo of two women in white outfits walking hand in hand on a beach" style="left:11px;top:53px;width:343px;height:257px;background:linear-gradient(180deg,#8e8e8e 0%,#bcbcbc 18%,#e6e6e6 45%,#cfcfcf 70%,#a3a3a3 100%)"></div>
  <svg style="left:285px;top:60px" width="66" height="9" viewBox="0 0 66 9" fill="none" stroke="#fff" stroke-width="1">
    <circle cx="4" cy="4" r="2.4"/><line x1="5.8" y1="5.8" x2="7.5" y2="7.5"/>
    <circle cx="16" cy="3" r="1.6"/><path d="M13 7.5a3 2 0 0 1 6 0"/>
    <path d="M25 2h1.4l1 4h4l1-3h-5.3"/><circle cx="28" cy="7.6" r=".5"/><circle cx="31" cy="7.6" r=".5"/>
    <path d="M40 7.5l-3-3a1.6 1.6 0 0 1 3-1.6a1.6 1.6 0 0 1 3 1.6z" fill="#fff"/>
    <rect x="43" y="0" width="4" height="4" fill="var(--gold)" stroke="none"/>
    <circle cx="59" cy="4" r="3"/><ellipse cx="59" cy="4" rx="1.3" ry="3"/><line x1="56" y1="4" x2="62" y2="4"/>
  </svg>
  <div style="left:230px;top:197px;width:124px;height:85px;background:var(--black)"></div>
  <div style="left:239px;top:208px;color:#fff;font-size:10.5px;font-weight:300;letter-spacing:1.2px;white-space:nowrap">FREE <b style="font-weight:800">SHIPPING</b></div>
  <div style="left:239px;top:225px;color:#fff;font-size:7px;letter-spacing:1px">GREATER THAN $$</div>
  <div style="left:239px;top:245px;width:75px;color:#fff;font-size:3.6px;line-height:1.3">Lorem ipsum dolor sit amet, consectetuer adipiscing elit, sed diam <u><b>nonummy nibh euismod</b></u> tincidunt ut laoreet dolore magna aliquam erat volutpat.</div>
  <svg class="go" style="left:320px;top:253px" viewBox="0 0 24 12"><path d="M2 6h19M16 1.5l5 4.5-5 4.5"/></svg>

  <div class="section-title" style="top:327px">LATEST ARRIVALS</div>

  <div role="img" aria-label="Black and white portrait of a woman in a tweed cap" style="left:0;top:353px;width:124px;height:267px;background:linear-gradient(180deg,#5a5a5a 0%,#b8b8b8 22%,#8a8a8a 42%,#2a2a2a 58%,#000 70%)"></div>
  <div class="tile-text" style="left:20px;top:530px;width:90px;text-align:right">DESIGNER<br><b>HATS</b><small style="font-size:7.5px">great deals</small></div>
  <svg class="go" style="left:88px;top:594px" viewBox="0 0 24 12"><path d="M2 6h19M16 1.5l5 4.5-5 4.5"/></svg>

  <div role="img" aria-label="Soft beige portrait of a woman wearing gold earrings" style="left:124px;top:353px;width:242px;height:134px;background:linear-gradient(100deg,#cdb89c 0%,#e3d6c5 35%,#efe4d6 60%,#d7bfa2 85%,#c9a57c 100%)"></div>
  <div class="tile-text" style="left:140px;top:380px">NEW<br>SUMMER<br><b>STOCK</b><small>ready</small></div>
  <svg class="go" style="left:142px;top:452px" viewBox="0 0 24 12"><path d="M2 6h19M16 1.5l5 4.5-5 4.5"/></svg>

  <div role="img" aria-label="Grey fashion photo of a woman in a light office suit" style="left:124px;top:487px;width:118px;height:133px;background:linear-gradient(180deg,#8f8f95,#a4a4a8 50%,#8c8a88)"></div>
  <div class="tile-text" style="left:130px;top:535px;width:97px;text-align:right">OFFICE<br><b>SUITS</b><small>hot sale</small></div>
  <svg class="go" style="left:203px;top:594px" viewBox="0 0 24 12"><path d="M2 6h19M16 1.5l5 4.5-5 4.5"/></svg>

  <div role="img" aria-label="Photo of legs in yellow ankle boots beside a bar stool" style="left:242px;top:487px;width:124px;height:133px;background:linear-gradient(180deg,#2a2f4a 0%,#3a2c26 40%,#6b5140 65%,#c9962e 85%,#8a7a62 100%)"></div>

  <div class="product-photo" role="img" aria-label="Model in a black leather jacket" style="left:50px;top:644px;width:80px;height:110px"></div>
  <div class="product-photo" role="img" aria-label="Model in a black jacket" style="left:143px;top:644px;width:80px;height:110px"></div>
  <div class="product-photo" role="img" aria-label="Model in a black jacket" style="left:234px;top:644px;width:81px;height:110px"></div>
  <div class="product-title" style="left:50px;top:765px;width:80px">LEATHER</div>
  <div class="product-note" style="left:50px;top:774px;width:80px">great new jackets</div>
  <div class="product-title" style="left:143px;top:765px;width:80px">WEDDINGS</div>
  <div class="product-note" style="left:143px;top:774px;width:80px">top outfits for big days</div>
  <div class="product-title" style="left:234px;top:765px;width:81px">SUMMER</div>
  <div class="product-note" style="left:234px;top:774px;width:81px">from shades to sunshine</div>

  <div class="product-photo" role="img" aria-label="Model in a black leather jacket" style="left:50px;top:795px;width:80px;height:110px"></div>
  <div class="product-photo" role="img" aria-label="Model in a black jacket" style="left:143px;top:795px;width:80px;height:110px"></div>
  <div class="product-photo" role="img" aria-label="Model in a black jacket" style="left:234px;top:795px;width:81px;height:110px"></div>
  <div class="product-title" style="left:50px;top:915px;width:80px">LEATHER</div>
  <div class="product-note" style="left:50px;top:924px;width:80px">great new jackets</div>
  <div class="product-title" style="left:143px;top:915px;width:80px">WEDDINGS</div>
  <div class="product-note" style="left:143px;top:924px;width:80px">top outfits for big days</div>
  <div class="product-title" style="left:234px;top:915px;width:81px">SUMMER</div>
  <div class="product-note" style="left:234px;top:924px;width:81px">from shades to sunshine</div>
  <div class="more" style="left:287px;top:939px">MORE &gt;</div>

  <div class="section-title" style="top:953px;left:-7px">SOCIAL MEDIA</div>
  <div class="social-avatar" role="img" aria-label="Social post photo of a model by the sea" style="left:-17px;top:979px"></div>
  <div class="social-avatar" role="img" aria-label="Social post photo of a model by the sea" style="left:45px;top:979px"></div>
  <div class="social-avatar" role="img" aria-label="Social post photo of a model by the sea" style="left:107px;top:979px"></div>
  <div class="social-avatar" role="img" aria-label="Social post photo of a model by the sea" style="left:169px;top:979px"></div>
  <div class="social-avatar" role="img" aria-label="Social post photo of a model by the sea" style="left:231px;top:979px"></div>
  <div class="social-avatar" role="img" aria-label="Social post photo of a model by the sea" style="left:293px;top:979px"></div>
  <div class="social-avatar" role="img" aria-label="Social post photo of a model by the sea" style="left:355px;top:979px"></div>
  <div class="social-caption" style="left:-24px;top:1029px">@ossa.style account<br>GREAT NEW JACKETS</div>
  <div class="social-caption" style="left:38px;top:1029px">@ossa.style account<br>GREAT NEW JACKETS</div>
  <div class="social-caption" style="left:100px;top:1029px">@ossa.style account<br>GREAT NEW JACKETS</div>
  <div class="social-caption" style="left:162px;top:1029px">@ossa.style account<br>GREAT NEW JACKETS</div>
  <div class="social-caption" style="left:224px;top:1029px">@ossa.style account<br>GREAT NEW JACKETS</div>
  <div class="social-caption" style="left:286px;top:1029px">@ossa.style account<br>GREAT NEW JACKETS</div>

  <footer class="footer" style="top:1050px">
    <div class="brand-name">OSSA</div>
    <p class="footer-copy">Lorem ipsum dolor sit amet, consectetuer adipiscing elit, sed diam nonummy nibh euismod tincidunt ut laoreet dolore magna aliquam erat volutpat.</p>
    <p class="footer-legal">©2021 COPYRIGHT/PRIVACY STATEMENT</p>
    <p class="subscribe">SUBSCRIBE</p>
    <p class="subscribe-note">get our newsletter and get the latest deals to your inbox</p>
    <p class="email-label">YOUR EMAIL</p><div class="email-line"></div>
    <svg class="go" viewBox="0 0 24 12"><path d="M2 6h19M16 1.5l5 4.5-5 4.5"/></svg>
    <div class="social-row"><span></span><span></span><span></span><span></span></div>
  </footer>
</section>

<!-- Catalogue page -->
<section class="page" style="left:415px;top:25px;width:366px;height:898px">
  <div class="brand-name">OSSA</div>
  <span class="nav" style="left:89px">LATEST ARRIVALS</span>
  <span class="nav" style="left:157px">CLOTHES</span>
  <span class="nav" style="left:204px">ON SALE</span>
  <span class="nav" style="left:245px">OSSA CLUB</span>
  <div role="img" aria-label="Black and white close-up portrait of a woman in a tweed cap" style="left:12px;top:56px;width:343px;height:152px;background:linear-gradient(100deg,#3a3a3a 0%,#d8d8d8 18%,#c2c2c2 38%,#9a9a9a 55%,#6e6e6e 72%,#e4e4e4 100%)"></div>
  <span class="filter" style="left:14px;top:228px">SHOPPING CART</span>
  <span class="filter" style="left:166px;top:228px">WISHLIST</span>
  <span class="filter" style="left:283px;top:227px">SEARCH FILTER</span>

  <div class="product-photo" role="img" aria-label="Model in a black leather jacket" style="left:22px;top:252px;width:73px;height:100px"></div>
  <div class="product-photo" role="img" aria-label="Model in a black jacket" style="left:106px;top:252px;width:73px;height:100px"></div>
  <div class="product-photo" role="img" aria-label="Model in a black jacket" style="left:190px;top:252px;width:73px;height:100px"></div>
  <div class="product-photo" role="img" aria-label="Model in a black leather jacket" style="left:274px;top:252px;width:73px;height:100px"></div>
  <div class="product-photo" role="img" aria-label="Model in a black leather jacket" style="left:22px;top:389px;width:73px;height:100px"></div>
  <div class="product-photo" role="img" aria-label="Model in a black jacket" style="left:106px;top:389px;width:73px;height:100px"></div>
  <div class="product-photo" role="img" aria-label="Model in a black jacket" style="left:190px;top:389px;width:73px;height:100px"></div>
  <div class="product-photo" role="img" aria-label="Model in a black leather jacket" style="left:274px;top:389px;width:73px;height:100px"></div>
  <div class="product-photo" role="img" aria-label="Model in a black leather jacket" style="left:22px;top:527px;width:73px;height:100px"></div>
  <div class="product-photo" role="img" aria-label="Model in a black jacket" style="left:106px;top:527px;width:73px;height:100px"></div>
  <div class="product-photo" role="img" aria-label="Model in a black jacket" style="left:190px;top:527px;width:73px;height:100px"></div>
  <div class="product-photo" role="img" aria-label="Model in a black leather jacket" style="left:274px;top:527px;width:73px;height:100px"></div>
  <div class="product-photo" role="img" aria-label="Model in a black leather jacket" style="left:22px;top:665px;width:73px;height:100px"></div>
  <div class="product-photo" role="img" aria-label="Model in a black jacket" style="left:106px;top:665px;width:73px;height:100px"></div>
  <div class="product-photo" role="img" aria-label="Model in a black jacket" style="left:190px;top:665px;width:73px;height:100px"></div>
  <div class="product-photo" role="img" aria-label="Model in a black leather jacket" style="left:274px;top:665px;width:73px;height:100px"></div>

  <div class="card-icons" style="left:80px;top:354px">♥ ⌂</div><div class="card-icons" style="left:164px;top:354px">♥ ⌂</div><div class="card-icons" style="left:248px;top:354px">♥ ⌂</div><div class="card-icons" style="left:332px;top:354px">♥ ⌂</div>
  <div class="card-icons" style="left:80px;top:491px">♥ ⌂</div><div class="card-icons" style="left:164px;top:491px">♥ ⌂</div><div class="card-icons" style="left:248px;top:491px">♥ ⌂</div><div class="card-icons" style="left:332px;top:491px">♥ ⌂</div>
  <div class="card-icons" style="left:80px;top:629px">♥ ⌂</div><div class="card-icons" style="left:164px;top:629px">♥ ⌂</div><div class="card-icons" style="left:248px;top:629px">♥ ⌂</div><div class="card-icons" style="left:332px;top:629px">♥ ⌂</div>
  <div class="card-icons" style="left:80px;top:767px">♥ ⌂</div><div class="card-icons" style="left:164px;top:767px">♥ ⌂</div><div class="card-icons" style="left:248px;top:767px">♥ ⌂</div><div class="card-icons" style="left:332px;top:767px">♥ ⌂</div>

  <div class="product-title" style="left:22px;top:361px;width:73px">LEATHER</div><div class="product-note" style="left:22px;top:370px;width:73px">great new jackets</div>
  <div class="product-title" style="left:106px;top:361px;width:73px">WEDDINGS</div><div class="product-note" style="left:106px;top:370px;width:73px">top outfits for big days</div>
  <div class="product-title" style="left:190px;top:361px;width:73px">SUMMER</div><div class="product-note" style="left:190px;top:370px;width:73px">from shades to sunshine</div>
  <div class="product-title" style="left:274px;top:361px;width:73px">LEATHER</div><div class="product-note" style="left:274px;top:370px;width:73px">great new jackets</div>

  <div class="product-title" style="left:22px;top:498px;width:73px">LEATHER</div><div class="product-note" style="left:22px;top:507px;width:73px">great new jackets</div>
  <div class="product-title" style="left:106px;top:498px;width:73px">WEDDINGS</div><div class="product-note" style="left:106px;top:507px;width:73px">top outfits for big days</div>
  <div class="product-title" style="left:190px;top:498px;width:73px">SUMMER</div><div class="product-note" style="left:190px;top:507px;width:73px">from shades to sunshine</div>
  <div class="product-title" style="left:274px;top:498px;width:73px">LEATHER</div><div class="product-note" style="left:274px;top:507px;width:73px">great new jackets</div>

  <div class="product-title" style="left:22px;top:636px;width:73px">LEATHER</div><div class="product-note" style="left:22px;top:645px;width:73px">great new jackets</div>
  <div class="product-title" style="left:106px;top:636px;width:73px">WEDDINGS</div><div class="product-note" style="left:106px;top:645px;width:73px">top outfits for big days</div>
  <div class="product-title" style="left:190px;top:636px;width:73px">SUMMER</div><div class="product-note" style="left:190px;top:645px;width:73px">from shades to sunshine</div>
  <div class="product-title" style="left:274px;top:636px;width:73px">LEATHER</div><div class="product-note" style="left:274px;top:645px;width:73px">great new jackets</div>

  <div class="product-title" style="left:22px;top:774px;width:73px">LEATHER</div><div class="product-note" style="left:22px;top:783px;width:73px">great new jackets</div>
  <div class="product-title" style="left:106px;top:774px;width:73px">WEDDINGS</div><div class="product-note" style="left:106px;top:783px;width:73px">top outfits for big days</div>
  <div class="product-title" style="left:190px;top:774px;width:73px">SUMMER</div><div class="product-note" style="left:190px;top:783px;width:73px">from shades to sunshine</div>
  <div class="product-title" style="left:274px;top:774px;width:73px">LEATHER</div><div class="product-note" style="left:274px;top:783px;width:73px">great new jackets</div>
  <div class="more" style="left:315px;top:791px">MORE &gt;</div>

  <footer class="footer" style="top:806px">
    <div class="brand-name">OSSA</div>
    <p class="footer-copy">Lorem ipsum dolor sit amet, consectetuer adipiscing elit, sed diam nonummy nibh euismod tincidunt ut laoreet dolore magna aliquam erat volutpat.</p>
    <p class="footer-legal">©2021 COPYRIGHT/PRIVACY STATEMENT</p>
    <p class="subscribe">SUBSCRIBE</p>
    <p class="subscribe-note">get our newsletter and get the latest deals to your inbox</p>
    <p class="email-label">YOUR EMAIL</p><div class="email-line"></div>
    <svg class="go" viewBox="0 0 24 12"><path d="M2 6h19M16 1.5l5 4.5-5 4.5"/></svg>
    <div class="social-row"><span></span><span></span><span></span><span></span></div>
  </footer>
</section>

<!-- Product page -->
<section class="page" style="left:807px;top:25px;width:366px;height:425px">
  <div class="brand-name">OSSA</div>
  <span class="nav" style="left:89px">LATEST ARRIVALS</span>
  <span class="nav" style="left:157px">CLOTHES</span>
  <span class="nav" style="left:204px">ON SALE</span>
  <span class="nav" style="left:245px">OSSA CLUB</span>
  <div class="product-photo" role="img" aria-label="Model in a black leather jacket" style="left:130px;top:64px;width:112px;height:156px"></div>
  <div style="left:107px;top:158px;width:10px;height:10px;border-radius:50%;background:#000"></div>
  <div style="left:107px;top:175px;width:10px;height:10px;border-radius:50%;background:#c8b98b"></div>
  <div style="left:107px;top:192px;width:10px;height:10px;border-radius:50%;border:.7px solid #999"></div>
  <div style="left:107px;top:210px;width:10px;height:10px;border-radius:50%;background:#fbc8f3"></div>
  <div style="left:256px;top:138px;font-size:7px;line-height:18.3px;color:var(--tan);letter-spacing:1.5px">XS<br>S<br>M<br>L<br>XL</div>
  <div class="card-icons" style="left:237px;top:222px">⌂</div>
  <div class="product-title" style="left:136px;top:231px;width:100px">LEATHER</div>
  <div class="product-note" style="left:136px;top:240px;width:100px">great new jackets</div>
  <div style="left:136px;top:253px;width:100px;text-align:center;font-size:7.5px;letter-spacing:2px;color:var(--tan)">$$$</div>
  <span class="filter" style="left:12px;top:295px">SHOPPING CART</span>
  <span class="filter" style="left:164px;top:295px">WISHLIST</span>
  <span class="filter" style="left:280px;top:294px">SEARCH FILTER</span>
  <footer class="footer" style="top:333px">
    <div class="brand-name">OSSA</div>
    <p class="footer-copy">Lorem ipsum dolor sit amet, consectetuer adipiscing elit, sed diam nonummy nibh euismod tincidunt ut laoreet dolore magna aliquam erat volutpat.</p>
    <p class="footer-legal">©2021 COPYRIGHT/PRIVACY STATEMENT</p>
    <p class="subscribe">SUBSCRIBE</p>
    <p class="subscribe-note">get our newsletter and get the latest deals to your inbox</p>
    <p class="email-label">YOUR EMAIL</p><div class="email-line"></div>
    <svg class="go" viewBox="0 0 24 12"><path d="M2 6h19M16 1.5l5 4.5-5 4.5"/></svg>
    <div class="social-row"><span></span><span></span><span></span><span></span></div>
  </footer>
</section>

<!-- Login page -->
<section class="page" style="left:807px;top:474px;width:366px;height:277px">
  <div class="brand-name">OSSA</div>
  <span class="nav" style="left:89px">LATEST ARRIVALS</span>
  <span class="nav" style="left:157px">CLOTHES</span>
  <span class="nav" style="left:204px">ON SALE</span>
  <span class="nav" style="left:245px">OSSA CLUB</span>
  <div class="login-title" style="left:90px;top:76px">LOGIN</div>
  <div class="field-label" style="left:91px;top:96px">EMAIL</div>
  <div class="field-label" style="left:91px;top:108px">PASSWORD</div>
  <div class="field-line" style="left:141px;top:100px"></div>
  <div class="field-line" style="left:141px;top:114px"></div>
  <svg class="go" style="left:250px;top:100px;width:30px;height:15px" viewBox="0 0 24 12"><path d="M2 6h19M16 1.5l5 4.5-5 4.5"/></svg>
  <div style="left:91px;top:134px;font-size:10px;letter-spacing:1.2px;font-weight:300;white-space:nowrap">with <span style="font-weight:300">Friendnet</span> or <span style="font-weight:300">Seekly</span></div>
  <footer class="footer" style="top:185px">
    <div class="brand-name">OSSA</div>
    <p class="footer-copy">Lorem ipsum dolor sit amet, consectetuer adipiscing elit, sed diam nonummy nibh euismod tincidunt ut laoreet dolore magna aliquam erat volutpat.</p>
    <p class="footer-legal">©2021 COPYRIGHT/PRIVACY STATEMENT</p>
    <p class="subscribe">SUBSCRIBE</p>
    <p class="subscribe-note">get our newsletter and get the latest deals to your inbox</p>
    <p class="email-label">YOUR EMAIL</p><div class="email-line"></div>
    <svg class="go" viewBox="0 0 24 12"><path d="M2 6h19M16 1.5l5 4.5-5 4.5"/></svg>
    <div class="social-row"><span></span><span></span><span></span><span></span></div>
  </footer>
</section>

<!-- Account page -->
<section class="page" style="left:807px;top:774px;width:366px;height:277px">
  <div class="brand-name">OSSA</div>
  <span class="nav" style="left:89px">LATEST ARRIVALS</span>
  <span class="nav" style="left:157px">CLOTHES</span>
  <span class="nav" style="left:204px">ON SALE</span>
  <span class="nav" style="left:245px">OSSA CLUB</span>
  <div role="img" aria-label="Profile photo of the account holder" style="left:20px;top:67px;width:40px;height:40px;border-radius:50%;background:radial-gradient(circle at 45% 45%,#d9b49a,#7a5a48 70%,#4a3a30)"></div>
  <div style="left:88px;top:67px;font-size:11px;font-weight:300;letter-spacing:1.5px">Hi, Name</div>
  <div class="account-item" style="left:88px;top:88px">email:<small>change password</small></div>
  <div class="account-item" style="left:88px;top:108px">address:<small>map</small></div>
  <div class="account-item" style="left:88px;top:130px">order history</div>
  <div class="account-item" style="left:88px;top:147px">shopping cart</div>
  <footer class="footer" style="top:185px">
    <div class="brand-name">OSSA</div>
    <p class="footer-copy">Lorem ipsum dolor sit amet, consectetuer adipiscing elit, sed diam nonummy nibh euismod tincidunt ut laoreet dolore magna aliquam erat volutpat.</p>
    <p class="footer-legal">©2021 COPYRIGHT/PRIVACY STATEMENT</p>
    <p class="subscribe">SUBSCRIBE</p>
    <p class="subscribe-note">get our newsletter and get the latest deals to your inbox</p>
    <p class="email-label">YOUR EMAIL</p><div class="email-line"></div>
    <svg class="go" viewBox="0 0 24 12"><path d="M2 6h19M16 1.5l5 4.5-5 4.5"/></svg>
    <div class="social-row"><span></span><span></span><span></span><span></span></div>
  </footer>
</section>

</body>
</html>
```